ko rim magazine

just need coupons of real customers made for my magazine, I have the layout or temp lets of the magazine i just need the coupons to be made and plug-in. i have examples, of the ads or coupons, I'm sure they will need to redone. and in a section of the magazine their in a church directory. with this section , i need the pic of the pastor plug in with their church information and in do have some ex-samples of that as well. with the websites of the businesses. if you need to grab an image from their site . you'll be able to do so. all of the business are in the upload section , these are small base business so a lot of the ads and logos need redone any way . so i will look at it and let you know.

P.S with the new coupons and logos I'm trying to impress these customers to stay with the magazine

Target Market(s)

small businesses

Requirements
Must have
• good graphics
Should not have
• not pixelated graphics

```html
<!DOCTYPE html>
<html lang="en">
<head>
<meta charset="utf-8">
<title>Harlan Chiropractic Center – Coupon</title>
<link rel="stylesheet" href="https://fonts.googleapis.com/css2?family=Arimo:wght@700&display=swap">
<style>
  :root {
    --canvas-grey: #808080;
    --panel-blue: #00ccff;
    --text-white: #ffffff;
  }
  html, body {
    margin: 0;
    padding: 0;
    width: 1200px;
    height: 1200px;
    overflow: hidden;
    background: var(--canvas-grey);
  }
  .coupon {
    display: block;
    width: 1200px;
    height: 1200px;
  }
  .coupon-panel { fill: var(--panel-blue); }
  .coupon-text {
    fill: var(--text-white);
    font-family: "Arimo", Arial, Helvetica, sans-serif;
    font-weight: 700;
  }
  .business-name { font-size: 203px; }
  .business-type { font-size: 65px; letter-spacing: 1px; }
  .business-details { font-size: 65px; letter-spacing: 1px; }
</style>
</head>
<body>
<svg class="coupon" viewBox="0 0 1200 1200" xmlns="http://www.w3.org/2000/svg">
  <rect class="coupon-panel" x="59" y="315" width="1082" height="612"/>
  <text class="coupon-text business-name" x="600" y="531" text-anchor="middle" textLength="907" lengthAdjust="spacing">HARLAN</text>
  <text class="coupon-text business-type" x="600" y="660" text-anchor="middle">CHIROPRACTIC CENTER LLC</text>
  <text class="coupon-text business-details" x="600" y="732" text-anchor="middle">318 Birch Avenue</text>
  <text class="coupon-text business-details" x="600" y="803" text-anchor="middle">Brookvale,PA</text>
  <text class="coupon-text business-details" x="600" y="874" text-anchor="middle">555-014-2200</text>
</svg>
</body>
</html>
```